Larkmoor Health- Core Values Graphic for Visual Appeal

I would like a poster that could take these written core values from our organization and create a graphic that we could use for our staff and employees. I would also like to incorporate our branding into this project. Thank you!

Target Market(s)

To helps patients and employees understand the core values of our organization

Industry/Entity Type

Healthcare

Requirements
Must have
• Match our branding
Nice to have
• Please use your creativity!
Should not have
• Overly complex/ busy

```html
<!DOCTYPE html>
<html lang="en">
<head>
<meta charset="utf-8">
<title>Larkmoor Health – Core Values</title>
<link href="https://fonts.googleapis.com/css2?family=Source+Sans+3:wght@400;700&display=swap" rel="stylesheet">
<style>
  :root {
    --teal: #007b8d;
    --teal-heading: #0a7a8b;
    --teal-soft: #4a97aa;
    --sky: #b4dcf5;
    --mist: #e7f2fb;
    --accent: #2aa8e0;
    --ink: #3d3d3d;
    --paper: #ffffff;
  }
  * { margin: 0; padding: 0; box-sizing: border-box; }
  html, body { width: 848px; height: 1200px; overflow: hidden; background: var(--paper); }
  .poster {
    position: relative;
    width: 848px;
    height: 1200px;
    overflow: hidden;
    font-family: "Source Sans 3", sans-serif;
    color: var(--ink);
    background: var(--paper);
  }
  .backdrop { position: absolute; inset: 0; }
  .brand {
    position: absolute;
    left: 70px;
    top: 92px;
    display: flex;
    align-items: center;
    gap: 10px;
  }
  .brand-dot {
    width: 18px; height: 18px; border-radius: 50%;
    background: var(--accent);
  }
  .brand-name {
    font-size: 22px;
    font-weight: 700;
    color: var(--ink);
    line-height: 1;
  }
  .intro {
    position: absolute;
    left: 49px;
    top: 214px;
    font-size: 24px;
    line-height: 25.6px;
    white-space: nowrap;
    color: #444;
  }
  .value { position: absolute; }
  .value-title {
    display: inline-block;
    font-size: 22px;
    font-weight: 700;
    color: var(--teal-heading);
    line-height: 1;
    padding-bottom: 3px;
    border-bottom: 2.5px solid var(--teal-heading);
    margin-bottom: 9px;
  }
  .value-text {
    font-size: 14.5px;
    line-height: 18.8px;
    white-space: nowrap;
  }
  .value--family { left: 49px; top: 353px; }
  .value--excellence { right: 41px; top: 516px; text-align: right; }
  .value--excellence .value-title { margin-right: 7px; }
  .value--integrity { left: 49px; top: 696px; }
  .value--service { right: 41px; top: 998px; text-align: right; }
  .value--service .value-title { color: var(--paper); border-color: var(--paper); margin-right: 24px; }
  .value--service .value-text { color: var(--paper); }
</style>
</head>
<body>
<main class="poster">
  <svg class="backdrop" width="848" height="1200" viewBox="0 0 848 1200" aria-hidden="true">
    <!-- faint cross on the right -->
    <g transform="translate(790 335) rotate(-23)" fill="var(--mist)">
      <rect x="-40" y="-175" width="80" height="350"/>
      <rect x="-150" y="-40" width="300" height="80"/>
    </g>
    <!-- top wave -->
    <path d="M236 0 C300 60 400 130 530 144 C640 152 760 128 848 122 L848 0 Z" fill="var(--teal)"/>
    <!-- small crosses -->
    <g fill="var(--sky)">
      <rect x="197" y="544" width="11" height="35"/>
      <rect x="185" y="556" width="35" height="11"/>
      <rect x="101" y="590" width="22" height="71"/>
      <rect x="76" y="614" width="72" height="23"/>
    </g>
    <!-- bottom wave -->
    <path d="M0 893 C180 852 420 882 590 902 C700 914 800 872 848 768 L848 1200 L0 1200 Z" fill="var(--teal)"/>
    <!-- white swoosh -->
    <path d="M460 946 C630 958 770 920 848 880 L848 896 C770 940 630 960 460 946 Z" fill="var(--paper)"/>
    <!-- chevron -->
    <polyline points="125,962 25,1064 125,1166" fill="none" stroke="var(--teal-soft)" stroke-width="76"/>
  </svg>

  <div class="brand">
    <span class="brand-dot"></span>
    <span class="brand-name">Larkmoor Health</span>
  </div>

  <p class="intro">These core values are the spirit of who we are as a healthcare team.<br>They guide our actions, unite us in purpose, and ensure that we<br>provide world-class care while fostering a positive and supportive<br>atmosphere within our team:</p>

  <section class="value value--family">
    <h2 class="value-title">Family:</h2>
    <p class="value-text">At the heart of our mission is the commitment to provide<br>high-quality, affordable healthcare in a comforting and uplifting<br>family-oriented environment. Just as our community is our<br>extended family, every patient is a cherished member of our<br>healthcare family. We treat each individual with the same care,<br>compassion, and respect we would offer to our own loved ones.</p>
  </section>

  <section class="value value--excellence">
    <h2 class="value-title">Excellence:</h2>
    <p class="value-text">In line with our goal, we aspire not only to alleviate pain but also&nbsp;<br>to inspire patients to become active participants in their well-being.<br>We believe in empowering our patients through education and&nbsp;<br>compassion. Our pursuit of excellence is unwavering, driven&nbsp;<br>by our dedication to continuously improve our services at every level,<br>ensuring that our community receives nothing less than exceptional care.</p>
  </section>

  <section class="value value--integrity">
    <h2 class="value-title">Integrity:</h2>
    <p class="value-text">In our healthcare team, 'Integrity' is non-negotiable.<br>Our purpose is deeply rooted in ethics, integrity, and professional standards.<br>We operate with the utmost integrity in every aspect of our work,<br>adhering to the highest ethical principles. We understand that trust is the foundation of healthcare,<br>and we are committed to maintaining the trust our community places in us.</p>
  </section>

  <section class="value value--service">
    <h2 class="value-title">Service:</h2>
    <p class="value-text">Our vision is grounded in the belief that every person possesses the innate potential for true health.<br>We aim to facilitate the body's natural healing response by providing the highest level of service.<br>Our hope for each patient extends beyond healing; we aspire to help you fulfill your life's mission<br>and purpose abundantly, supporting you in your journey to well-being.</p>
  </section>
</main>
</body>
</html>
```